TORNWICK Pizza Flyer / Menu

Hello so its a new pizza shop called Tornwick. I need a flyer menu designed . it will be 30cm tall and 10.5cm wide. i made one which i have uploaded but as you can see im not very skillfull design wise. I did want the logo on the front with the photo of the counter in the middle and then half the pizza at the bottom. then on the back i wanted all the different toppings ( doesnt have to be the same pics as i have used ) and then drinks and desserts underneath and our contact details. I dont want to include our signature specials. Also facebook/twitter and instagram logos somewhere. the font i have been using is called 'AR CENA' i have attached a rough sketch i have put together to give you an idea too. thanks

Industry/Entity Type

Shop

```html
<!DOCTYPE html>
<html lang="en">
<head>
<meta charset="utf-8">
<title>Tornwick Pizza Flyer Menu</title>
<link href="https://fonts.googleapis.com/css2?family=Patrick+Hand&family=Arimo:wght@700&family=Fredoka:wght@500&display=swap" rel="stylesheet">
<style>
  :root {
    --page: #eeeeee;
    --board: #39393b;
    --board-dark: #2f2f31;
    --orange: #f7941d;
    --white: #ffffff;
    --ink: #232323;
    --band-light: #c4c4c4;
    --band-dark: #9c9c9c;
    --red: #e0283a;
  }
  * { margin: 0; padding: 0; box-sizing: border-box; }
  html, body { width: 915px; height: 1200px; overflow: hidden; }
  body {
    position: relative;
    background: radial-gradient(ellipse at center, #fafafa 0%, var(--page) 70%, #e2e2e2 100%);
    font-family: "Patrick Hand", "Comic Sans MS", cursive;
  }
  .panel {
    position: absolute;
    top: 108px;
    width: 344px;
    height: 982px;
    background: radial-gradient(ellipse at 50% 40%, var(--board) 0%, var(--board-dark) 100%);
    box-shadow: 0 2px 10px rgba(0,0,0,0.35);
    overflow: hidden;
  }
  .panel--front { left: 97px; }
  .panel--back { left: 474px; }
  .abs { position: absolute; }

  /* front */
  .front-tagline-top {
    top: 48px; width: 100%; text-align: center;
    color: var(--white); font-size: 30px; letter-spacing: 2px;
  }
  .front-mark {
    top: 90px; left: 96px; width: 154px; height: 154px;
    border-radius: 50%; background: var(--orange);
  }
  .front-name {
    top: 228px; width: 100%; text-align: center;
    color: var(--white); font-size: 58px; letter-spacing: 3px; line-height: 1;
  }
  .front-photo { top: 320px; left: 0; width: 344px; height: 350px; }
  .front-slogan {
    top: 712px; width: 100%; text-align: center;
    color: var(--orange); font-size: 33px; letter-spacing: 1px;
  }
  .front-pizza {
    top: 792px; left: 0; width: 344px; height: 190px;
    background: radial-gradient(ellipse at 55% 85%, #e0a85a 0%, #b4642c 35%, #5a5a3a 60%, transparent 78%);
  }

  /* back */
  .brand {
    top: 48px; left: 0; width: 100%; height: 70px;
  }
  .brand-mark {
    left: 14px; top: 12px; width: 48px; height: 48px;
    border-radius: 50%; background: var(--orange);
  }
  .brand-name {
    left: 76px; top: 2px; color: var(--white); font-size: 50px; letter-spacing: 2px; line-height: 1;
  }
  .brand-est {
    right: 42px; top: 50px; color: var(--white); font-size: 13px;
  }
  .brand-address {
    top: 122px; width: 100%; text-align: center;
    color: var(--white); font-size: 11px; letter-spacing: 0.3px;
  }
  .section { left: 0; width: 344px; }
  .section-tab {
    position: relative; height: 29px;
  }
  .section-tab svg { position: absolute; left: 0; top: 0; }
  .section-title {
    position: absolute; left: 16px; top: -1px;
    color: var(--orange); font-size: 27px; line-height: 1; letter-spacing: 1px;
  }
  .menu-list {
    list-style: none; height: 132px; padding-top: 5px;
    background: linear-gradient(180deg, var(--band-light) 0%, var(--band-dark) 100%);
  }
  .menu-item {
    position: relative; height: 32.5px; padding-left: 26px;
    color: var(--ink); font-size: 21px; line-height: 30px; letter-spacing: 0.5px;
  }
  .menu-item::before {
    content: ""; position: absolute; left: 7px; top: 10px;
    width: 10px; height: 10px; border-radius: 50%;
    background: var(--orange); border: 2px solid #ffd27a;
  }
  .price { position: absolute; right: 12px; top: 0; font-size: 22px; }
  .badge {
    display: inline-block; vertical-align: 3px; margin-left: 4px;
    background: var(--orange); color: var(--white);
    font-size: 10px; line-height: 14px; padding: 0 5px; border-radius: 8px;
  }
  .delivery {
    top: 740px; width: 100%; text-align: center;
    font-family: "Arimo", Arial, sans-serif; font-weight: 700;
    color: var(--orange); font-size: 19px; line-height: 30px;
  }
  .delivery small {
    display: block; font-size: 10px; line-height: 12px; font-weight: 700;
  }
  .phone {
    top: 822px; width: 100%; text-align: center;
    font-family: "Fredoka", sans-serif; font-weight: 500;
    color: var(--red); font-size: 40px; letter-spacing: 1.5px;
  }
  .follow {
    top: 888px; left: 5px;
    font-family: "Arimo", Arial, sans-serif; font-weight: 700;
    color: var(--orange); font-size: 15.5px; line-height: 23px;
  }
  .free-pizza {
    top: 936px; left: 5px; color: var(--orange); font-size: 31px; line-height: 1;
  }
  .social { top: 928px; left: 200px; display: flex; gap: 7px; }
  .social-square {
    width: 38px; height: 38px; border-radius: 5px;
    background: #6c8fbf;
  }
</style>
</head>
<body>

<section class="panel panel--front">
  <p class="abs front-tagline-top">DESIGNER PIZZA</p>
  <div class="abs front-mark"></div>
  <h1 class="abs front-name">TORNWICK</h1>

  <svg class="abs front-photo" viewBox="0 0 344 350" width="344" height="350">
    <polygon points="0,43 344,0 344,13 0,56" fill="var(--orange)"/>
    <polygon points="0,56 344,13 344,250 0,310" fill="url(#counterTones)" role="img" aria-label="Photo of the pizza topping counter with trays of fresh ingredients"/>
    <polygon points="0,310 344,250 344,262 0,325" fill="var(--orange)"/>
    <defs>
      <linearGradient id="counterTones" x1="0" y1="0" x2="1" y2="1">
        <stop offset="0" stop-color="#c9c1b5"/>
        <stop offset="0.45" stop-color="#8d6a4e"/>
        <stop offset="0.75" stop-color="#b9b4ad"/>
        <stop offset="1" stop-color="#e4e0da"/>
      </linearGradient>
    </defs>
  </svg>

  <p class="abs front-slogan">QUICK - KUSTOM - PIZZA</p>
  <div class="abs front-pizza" role="img" aria-label="Photo of pizza slices with herbs, tomatoes and chilli"></div>
</section>

<section class="panel panel--back">
  <header class="abs brand">
    <div class="abs brand-mark"></div>
    <p class="abs brand-name">TORNWICK</p>
    <p class="abs brand-est">EST 2016</p>
  </header>
  <p class="abs brand-address">27 THE PARADE, HOLLYBROOK, MERTON, SM9 4QX</p>

  <div class="abs section" style="top:164px">
    <div class="section-tab">
      <svg width="344" height="29"><polygon points="0,0 130,0 160,29 0,29" fill="#555557"/></svg>
      <h2 class="section-title">EXTRAS...</h2>
    </div>
    <ul class="menu-list">
      <li class="menu-item">SIDE SALAD<span class="price">2.49</span></li>
      <li class="menu-item">GARLIC BREAD<span class="price">2.49</span></li>
      <li class="menu-item">GAELIC BREAD WITH CHEESE<span class="price">2.99</span></li>
      <li class="menu-item">OLIVE POT<span class="price">1.49</span></li>
    </ul>
  </div>

  <div class="abs section" style="top:359px">
    <div class="section-tab">
      <svg width="344" height="29"><polygon points="0,0 130,0 160,29 0,29" fill="#555557"/></svg>
      <h2 class="section-title">DESSERTS...</h2>
    </div>
    <ul class="menu-list">
      <li class="menu-item">BANNACHOCA PIZZA !!!<span class="badge">Legendary</span><span class="price">3.99</span></li>
      <li class="menu-item">CREME BRULEE<span class="price">2.49</span></li>
      <li class="menu-item">TIRAMISU<span class="price">2.49</span></li>
      <li class="menu-item">CHOCO DREAM CAKE<span class="price">2.49</span></li>
    </ul>
  </div>

  <div class="abs section" style="top:553px">
    <div class="section-tab">
      <svg width="344" height="29"><polygon points="0,0 130,0 160,29 0,29" fill="#555557"/></svg>
      <h2 class="section-title">DRINKS...</h2>
    </div>
    <ul class="menu-list">
      <li class="menu-item">BLOOD ORANGE<span class="price">0.99</span></li>
      <li class="menu-item">ORANGEADE<span class="price">0.99</span></li>
      <li class="menu-item">LEMON<span class="price">0.99</span></li>
      <li class="menu-item">FIZZ COLA<span class="price">0.89</span></li>
    </ul>
  </div>

  <p class="abs delivery">WOOD STONE PIZZA DELIVERED<br>HOT YOUR DOOR STEP<small>MINIMUM ORDER £12</small></p>
  <p class="abs phone">00208 555 0192</p>
  <p class="abs follow">FOLLOW US FOR UPDATES, OFFERS<br>AND YOUR LUCKY ...</p>
  <p class="abs free-pizza">A FREE PIZZA</p>
  <div class="abs social">
    <div class="social-square"></div>
    <div class="social-square"></div>
    <div class="social-square"></div>
  </div>
</section>

</body>
</html>
```